Personal Development Business needs a Business Card Design Project

We need a buiness card design for a new Personal Development business based in S. NSW in Australia called "Willow Path Onward. Our target market is to women who are looking to re-enter the workforce, or already be in the workforce at the middle management level. As a result of consultations their outcomes will be, but not exclusive to: increased confidence, increased self esteem and self awareness, work-life balance, time management, positive thinking.
Behind the scenes of coaching and mentoring will be a spiritual "bent".
Anticipate a beautiful candle as a possible background - showing success and shining - see attachment which came off Pixelmarket. Colours - Unsure until I see something that "grabs my attention". Not esoteric fluffy design but something that suggests safe, professional, supportive of personal journey without being too corporate.
Look forward to what you come up with.
Target Market(s)
Some designers have been requesting various bits of information.
Personal information. See attachment.
Two-sided please.
Gold lines at all four edges.
Many thanks
Ruth
Industry/Entity Type
Business
Look and feel
Each slider illustrates characteristics of the customer's brand and the style your logo design should communicate.

```html
<!DOCTYPE html>
<html lang="en">
<head>
<meta charset="utf-8">
<title>Willow Path Onward – Business Card</title>
<link rel="stylesheet" href="https://fonts.googleapis.com/css2?family=Abril+Fatface&family=Arimo:wght@400;700&display=swap">
<style>
  :root {
    --page-bg: #ece8e2;
    --kraft: #a86d3c;
    --kraft-dark: #8f5a2f;
    --photo-dark: #2c2925;
    --photo-mid: #5a5248;
    --photo-warm: #e9cfa4;
    --glow: #fff3d6;
    --text-light: #ffffff;
    --text-soft: #f3e6d6;
    --title-edge: #7a4a22;
  }
  * { margin: 0; padding: 0; box-sizing: border-box; }
  html, body { width: 1200px; height: 740px; overflow: hidden; }
  body {
    background: var(--page-bg);
    font-family: "Arimo", Arial, sans-serif;
    position: relative;
  }
  .card {
    position: absolute;
    top: 211px;
    width: 520px;
    height: 318px;
    overflow: hidden;
    border-radius: 3px;
    box-shadow: 0 6px 18px rgba(0,0,0,0.18);
  }
  .card--back { left: 50px; background: var(--kraft); }
  .card--front { left: 630px; }

  /* Back side */
  .back__photo-strip {
    position: absolute;
    left: 0; right: 0; bottom: 0;
    height: 74px;
    background: linear-gradient(90deg, var(--photo-dark) 0%, var(--photo-mid) 55%, var(--photo-warm) 100%);
  }
  .back__kraft {
    position: absolute;
    left: 0; top: 0; right: 0;
    height: 262px;
    background: linear-gradient(180deg, var(--kraft) 0%, var(--kraft-dark) 100%);
    clip-path: polygon(0 0, 100% 0, 100% 72%, 0 100%);
  }
  .back__identity {
    position: absolute;
    left: 34px; top: 78px;
    color: var(--text-light);
  }
  .back__name {
    font-weight: 700;
    font-size: 29px;
    letter-spacing: 0.3px;
    margin-bottom: 8px;
  }
  .back__credentials {
    font-size: 11.5px;
    line-height: 1.45;
    color: var(--text-soft);
  }
  .back__divider {
    position: absolute;
    left: 262px; top: 40px;
    width: 1px; height: 120px;
    background: var(--text-soft);
  }
  .back__contacts {
    position: absolute;
    left: 280px; top: 48px;
    list-style: none;
    color: var(--text-light);
    font-size: 12px;
  }
  .back__contacts li {
    display: flex;
    align-items: center;
    gap: 9px;
    height: 34px;
  }
  .back__contacts svg { width: 16px; height: 16px; flex: none; }
  .back__services {
    position: absolute;
    left: 30px; bottom: 86px;
    display: flex;
    gap: 22px;
    list-style: none;
    color: var(--text-light);
    font-size: 16px;
  }
  .back__services li { display: flex; align-items: center; gap: 6px; }
  .back__services li::before {
    content: "";
    width: 13px; height: 13px;
    border-radius: 50%;
    background: var(--text-light);
  }

  /* Front side */
  .front__photo {
    position: absolute; inset: 0;
    background:
      radial-gradient(circle at 76% 40%, var(--glow) 0%, var(--photo-warm) 12%, rgba(160,140,110,0.6) 28%, rgba(60,55,48,0) 48%),
      linear-gradient(160deg, var(--photo-mid) 0%, var(--photo-dark) 70%);
  }
  .front__brand {
    position: absolute;
    left: 40px; bottom: 62px;
    color: var(--text-light);
  }
  .front__title {
    font-family: "Abril Fatface", Georgia, serif;
    font-size: 40px;
    line-height: 1;
    letter-spacing: 0.5px;
    text-shadow: 2px 2px 0 var(--title-edge);
  }
  .front__tagline {
    font-weight: 700;
    font-size: 19px;
    margin-top: 6px;
    margin-left: 6px;
  }
</style>
</head>
<body>

<section class="card card--back" aria-label="Card back">
  <div class="back__photo-strip" role="img" aria-label="Candle holder with crystals on dark stone"></div>
  <div class="back__kraft"></div>

  <div class="back__identity">
    <h1 class="back__name">Ruth Halden</h1>
    <p class="back__credentials">Grad Dip (Mgt) RVU<br>BA American History (CTU)<br>Master NLP</p>
  </div>

  <div class="back__divider"></div>

  <ul class="back__contacts">
    <li>
      <svg viewBox="0 0 16 16" fill="none" stroke="#fff" stroke-width="1.2"><circle cx="8" cy="8" r="7"/><ellipse cx="8" cy="8" rx="3" ry="7"/><line x1="1" y1="8" x2="15" y2="8"/><line x1="2" y1="4.5" x2="14" y2="4.5"/><line x1="2" y1="11.5" x2="14" y2="11.5"/></svg>
      willowpathonward.com.au
    </li>
    <li>
      <svg viewBox="0 0 16 16"><rect x="0" y="0" width="16" height="16" rx="2" fill="#fff"/><path d="M5 3.5c-1 .5-1.5 1.5-1 3 .8 2.5 2.8 4.6 5.3 5.6 1.4.5 2.4 0 3-1l-1.8-1.6-1.2.8C8 9.5 6.5 8 5.7 6.8l.8-1.2z" fill="#a86d3c"/></svg>
      0400 555 218
    </li>
    <li>
      <svg viewBox="0 0 16 16"><rect x="0" y="2" width="16" height="12" fill="#fff"/><path d="M0 2l8 6 8-6" fill="none" stroke="#a86d3c" stroke-width="1.3"/></svg>
      ruthatwillow@vinemail.com.au
    </li>
  </ul>

  <ul class="back__services">
    <li>Self Awareness</li>
    <li>Confidence</li>
    <li>Work-Life Balance</li>
  </ul>
</section>

<section class="card card--front" aria-label="Card front">
  <div class="front__photo" role="img" aria-label="Lit candle in a jewelled metal holder on dark stone"></div>
  <div class="front__brand">
    <h2 class="front__title">Willow Path Onward</h2>
    <p class="front__tagline">Personal Development</p>
  </div>
</section>

</body>
</html>
```